social interest sharing site needs a web site design

we need a web site design for a social web platform.
the site is one page(main page), that is split into 3 sections
each section is a different color(red,green and blue)
and a user can choose to share each of the sections.
any section/color will contain boxes , each box can contain different media types.

the media types:
* list of URLS
* list of articles including title + image + description
* list of videos
* thumbnails of images
* calender
* list of emails

the main content will look like corkboardly layout
multiple boxes each box can contain different type of content as described above

each color is a different tab
each tab will have layout like corkboardly
Updates

please read the last description update.
and i uploaded an image that can explain the requirements better

thanks
Oren
 

Industry/Entity Type

Media

```html
<!DOCTYPE html>
<html lang="en">
<head>
<meta charset="utf-8">
<title>Tabnest.me</title>
<link href="https://fonts.googleapis.com/css2?family=Open+Sans:wght@300;400;600;700&display=swap" rel="stylesheet">
<style>
:root{
  --bg:#efebe6;--ink:#333;--muted:#777;--dark:#1c1c1c;
  --red:#c8102e;--green:#17936f;--blue:#0f5aa8;
  --salmon:#f36b6b;--teal:#4fd6bf;--navy:#4a6390;--gold:#f7c55a;
  --tag:#f6b73c;--tagtext:#fff;--signup:#1a9a7d;--arrow:#ee3a1c;
  --foot:#4a6fb5;--calgreen:#b6d58c;--intro:#8a7250;--panel:#fff;
}
*{box-sizing:border-box;margin:0;padding:0}
html,body{width:758px;height:1200px;overflow:hidden}
body{position:relative;background:var(--bg);font-family:"Open Sans",Arial,sans-serif;color:var(--ink)}
.abs{position:absolute}
.topbar{left:216px;top:0;width:542px;height:84px;background:var(--dark)}
.topbar-edge{left:216px;top:84px}
.tab{top:0;width:72px;height:138px;color:#fff;font-size:9px;padding:102px 0 0 10px;line-height:1.25}
.tab.home{left:0;background:var(--red)}
.tab.fav{left:72px;background:var(--green)}
.tab.apps{left:144px;background:var(--blue)}
.brand{left:20px;top:32px;color:#fff;font-size:26px;font-weight:700;letter-spacing:-.5px}
.brand small{font-size:15px;font-weight:600}
.icon-btn{top:22px;width:41px;height:41px;background:#3d74c4;border-radius:4px}
.login{left:588px;top:32px;color:#fff;font-size:14px;font-weight:600}
.signup{left:634px;top:29px;width:84px;height:24px;border-radius:3px;background:var(--signup);color:#fff;font-size:14px;font-weight:600;text-align:center;line-height:24px}
.following{left:223px;top:96px;font-size:10px;font-weight:600;line-height:1.2;color:#222}
.pill{top:96px;width:95px;height:25px;background:var(--tag);border-radius:2px;color:var(--tagtext);font-size:8px;line-height:1.15;padding:3px 8px;box-shadow:0 1px 2px rgba(0,0,0,.2)}
.settings{left:0;top:166px;width:28px;height:30px;background:#888;border-radius:0 3px 3px 0}
.intro{left:88px;top:159px;width:590px;text-align:center;font-size:12.5px;line-height:1.35;color:var(--intro)}
.panel{background:var(--panel);box-shadow:0 1px 3px rgba(0,0,0,.15)}
.panel-title{height:40px;color:#fff;font-size:18px;font-weight:400;padding:6px 0 0 18px}
.corner{width:16px;height:16px;background:var(--arrow)}
.card{left:62px;width:255px;height:90px;background:#f4f4f4;border:1px solid #ddd;box-shadow:0 1px 2px rgba(0,0,0,.15)}
.card-photo{left:0;top:0;width:90px;height:88px;background:linear-gradient(160deg,#3a3a3a,#121212 70%,#555)}
.card-bar{left:90px;top:0;width:3px;height:88px}
.card-name{left:102px;top:14px;font-size:11px;color:#333}
.card-handle{left:102px;top:29px;font-size:7px;color:#888}
.card-desc{left:102px;top:40px;width:150px;font-size:6.8px;line-height:1.4;color:#555;white-space:nowrap}
.card-foot{left:93px;top:68px;width:160px;height:20px;background:#e6e6e6;font-size:7px;font-weight:700;padding:5px 0 0 10px}
.read{left:200px;top:8px;width:44px;height:18px;color:#fff;font-size:7px;font-weight:700;text-align:center;line-height:18px;border-radius:2px}
.urls{left:52px;top:686px;width:270px;height:192px;font-size:7.6px;line-height:13.6px;color:#333;white-space:nowrap;overflow:hidden}
.urls .hl{color:#2a6fd6;text-decoration:underline}
.scroll{left:327px;top:682px;width:5px;height:196px;background:#e2e2e2;border-radius:3px}
.scroll i{position:absolute;left:0;top:26px;width:5px;height:40px;background:#bbb;border-radius:3px}
.video{left:368px;width:195px;height:118px;background:linear-gradient(160deg,#2a3b45,#0d1418 60%,#1d2a30);box-shadow:0 2px 4px rgba(0,0,0,.35)}
.video-ctrl{left:0;bottom:0;width:195px;height:14px;background:#111;color:#ddd;font-size:6px;line-height:14px;padding-left:112px}
.video-ctrl i{position:absolute;left:12px;top:6px;width:90px;height:2px;background:#b33}
.v-title{left:571px;font-size:9.5px;text-decoration:underline;line-height:1.3;width:135px}
.v-text{left:571px;width:135px;font-size:7.2px;line-height:1.4;color:#777}
.watch{left:571px;width:44px;height:18px;border-radius:2px;color:#fff;font-size:7px;font-weight:700;text-align:center;line-height:18px}
.thumb{width:72px;height:72px;border:2px solid #fff;box-shadow:0 0 0 1px #bbb,0 2px 3px rgba(0,0,0,.25);background:linear-gradient(170deg,#6c8560,#3a3028 55%,#243a20)}
.thumb span{position:absolute;left:0;bottom:4px;width:100%;text-align:center;color:#fff;font-size:5px;font-weight:700;line-height:1.2}
.cal-head{left:60px;top:912px;width:258px;height:32px;background:var(--calgreen);text-align:center;font-size:13px;font-weight:600;color:#555;line-height:32px}
.cal-nav{top:912px;width:18px;height:32px;background:#6e7f86}
.cal{left:60px;top:960px;width:258px;border-collapse:collapse;table-layout:fixed;font-size:9.5px;color:#666;text-align:center}
.cal th{height:16px;font-weight:600;color:#333}
.cal td{border:1px solid #e3e3e3;height:27.5px}
.cal td.off{color:#ccc}
.cal td.today{background:#c4bd8e}
.note{left:166px;top:1043px;width:117px;height:38px;background:#fff;border:1px solid #ccc;box-shadow:0 2px 4px rgba(0,0,0,.25);font-size:6px;color:#aaa}
.footer{left:0;top:1162px;width:758px;height:38px;background:var(--foot);color:#fff;font-size:9px;line-height:38px}
</style>
</head>
<body>

<div class="abs topbar"></div>
<svg class="abs topbar-edge" width="542" height="6" viewBox="0 0 542 6" aria-hidden="true">
  <path d="M0 0H542V0L539 5 536 0 533 5 530 0 527 5 524 0 521 5 518 0 515 5 512 0 509 5 506 0 503 5 500 0H0Z" fill="#1c1c1c"/>
</svg>

<div class="abs tab home">My home</div>
<div class="abs tab fav">My favorites<br>videos</div>
<div class="abs tab apps">Personal<br>apps</div>
<div class="abs brand">Tabnest<small>.me</small></div>

<div class="abs icon-btn" style="left:372px"></div>
<div class="abs icon-btn" style="left:416px"></div>
<div class="abs icon-btn" style="left:461px">
  <svg width="41" height="41" viewBox="0 0 41 41" aria-hidden="true"><text x="20.5" y="29" text-anchor="middle" fill="#fff" font-family="Open Sans,sans-serif" font-size="24" font-weight="700">?</text></svg>
</div>
<div class="abs icon-btn" style="left:505px">
  <svg width="41" height="41" viewBox="0 0 41 41" aria-hidden="true"><circle cx="18" cy="18" r="7" stroke="#fff" stroke-width="3" fill="none"/><line x1="23" y1="23" x2="30" y2="30" stroke="#fff" stroke-width="4" stroke-linecap="round"/></svg>
</div>
<div class="abs login">Login</div>
<div class="abs signup">Sign up</div>

<div class="abs following">Following<br>TABNEST</div>
<div class="abs pill" style="left:277px">Dalias favorites<br>videos</div>
<div class="abs pill" style="left:390px">Mayas pics +<br>favorites links</div>
<div class="abs pill" style="left:502px">Family weekly<br>calendar and notes</div>

<div class="abs settings">
  <svg width="28" height="30" viewBox="0 0 28 30" aria-hidden="true"><circle cx="14" cy="15" r="6" fill="none" stroke="#222" stroke-width="4" stroke-dasharray="3 2"/><circle cx="14" cy="15" r="2.5" fill="#222"/></svg>
</div>

<p class="abs intro">This is Pixelforge's version &nbsp;of Lorem Ipsum. Proin gravida nibh vel velit auctor aliquet. Aenean sollicitudin, lorem quis bibendum auctor, nisi elit consequat ipsum, nec sagittis sem nibh id elit. Duis sed odio sit amet nibh vulputate cursus a sit amet mauris.</p>

<!-- Articles -->
<section class="abs panel" style="left:40px;top:229px;width:298px;height:377px"></section>
<h2 class="abs panel-title" style="left:40px;top:236px;width:200px;background:var(--salmon)">List of Articles</h2>
<div class="abs corner" style="left:322px;top:230px"></div>

<article class="abs card" style="top:284px">
  <div class="abs card-photo" role="img" aria-label="Photo of a magician stacking coloured cups"></div>
  <div class="abs card-bar" style="background:#79b829"></div>
  <div class="abs card-name">Clara Winters</div>
  <div class="abs card-handle">@ClaraW</div>
  <div class="abs card-desc">Sed posuere consectetur est at lobortis.<br>Integer posuere erat a ante venenatis dapibus</div>
  <div class="abs card-foot">1 245 Followers</div>
  <div class="abs read" style="background:#78b52c">Read More</div>
</article>
<article class="abs card" style="top:395px">
  <div class="abs card-photo" role="img" aria-label="Photo of a magician stacking coloured cups"></div>
  <div class="abs card-bar" style="background:#2a7bd1"></div>
  <div class="abs card-name">Nora Fields</div>
  <div class="abs card-handle">@NoraF</div>
  <div class="abs card-desc">Sed posuere consectetur est at lobortis.<br>Integer posuere erat a ante venenatis dapibus</div>
  <div class="abs card-foot">68 903 Followers</div>
  <div class="abs read" style="background:#2a7bd1">Read More</div>
</article>
<article class="abs card" style="top:502px">
  <div class="abs card-photo" role="img" aria-label="Photo of a magician stacking coloured cups"></div>
  <div class="abs card-bar" style="background:#d4232a"></div>
  <div class="abs card-name">Hanna Brooks</div>
  <div class="abs card-handle">@HannaB</div>
  <div class="abs card-desc">Sed posuere consectetur est at lobortis.<br>Integer posuere erat a ante venenatis dapibus</div>
  <div class="abs card-foot">384 Followers</div>
  <div class="abs read" style="background:#d4232a">Read More</div>
</article>

<!-- URLs -->
<section class="abs panel" style="left:40px;top:620px;width:298px;height:274px"></section>
<h2 class="abs panel-title" style="left:40px;top:626px;width:199px;background:var(--teal)">List of URL</h2>
<div class="abs corner" style="left:322px;top:621px"></div>
<div class="abs urls">
http://www.corkboardly.com/search/pins/?q=videos<br>
file:///C:/Users/Dana/Desktop/tabnest%20copy.jpg<br>
http://blog.northcorner.com/2013/12/premium-word-<br>
press-themes-responsive-retina-ready/<br>
http://www.corkboardly.com/pin/410531322254219328/<br>
http://www.corkboardly.com/<br>
<span class="hl">http://jobs.crowdsketch.com/job.aspx?id=340052&amp;src=rec</span><br>
http://pitchboard.com/web-design/contests/create-homep-<br>
age-brand-high-end-artisan-perfume-china-273917/brief<br>
http://pitchboard.com/web-design/contests/create-homep-<br>
age-brand-high-end-artisan-perfume-china-273917/entries<br>
http://www.crowdsketch.com/myprofile.aspx<br>
http://www.crowdsketch.com/contact.aspxhttp://pitch-<br>
board.com/web-design/contests/create-homepage-brand-high
</div>
<div class="abs scroll"><i></i></div>

<!-- Calendar -->
<section class="abs panel" style="left:40px;top:908px;width:298px;height:232px"></section>
<div class="abs cal-head">NOVEMBER</div>
<div class="abs cal-nav" style="left:42px">
  <svg width="18" height="32" viewBox="0 0 18 32" aria-hidden="true"><path d="M11 11 6 16 11 21" stroke="#fff" stroke-width="2" fill="none"/></svg>
</div>
<div class="abs cal-nav" style="left:318px">
  <svg width="18" height="32" viewBox="0 0 18 32" aria-hidden="true"><path d="M7 11 12 16 7 21" stroke="#fff" stroke-width="2" fill="none"/></svg>
</div>
<table class="abs cal">
  <tr><th>Mon</th><th>Tue</th><th>Wed</th><th>Thu</th><th>Fri</th><th>Sat</th><th>Sun</th></tr>
  <tr><td>1</td><td>2</td><td>3</td><td>4</td><td>5</td><td>6</td><td>7</td></tr>
  <tr><td>8</td><td>9</td><td>10</td><td>11</td><td>12</td><td>13</td><td>14</td></tr>
  <tr><td>15</td><td>16</td><td>17</td><td>18</td><td>19</td><td>20</td><td>21</td></tr>
  <tr><td>22</td><td>23</td><td>24</td><td>25</td><td>26</td><td>27</td><td>28</td></tr>
  <tr><td>29</td><td class="today">30</td><td>31</td><td class="off">1</td><td class="off">2</td><td class="off">3</td><td class="off">4</td></tr>
</table>
<div class="abs note">
  <div class="abs" style="left:6px;top:5px">I still need to do ...</div>
  <div class="abs" style="left:3px;top:21px;width:80px;height:13px;border:1px solid #ddd;padding:2px 3px;color:#777">17 November 2013</div>
  <div class="abs" style="left:86px;top:21px;width:27px;height:13px;background:#6fa5f0;color:#fff;text-align:center;line-height:13px">Go</div>
</div>

<!-- Videos -->
<section class="abs panel" style="left:356px;top:229px;width:362px;height:485px"></section>
<h2 class="abs panel-title" style="left:356px;top:236px;width:201px;background:var(--navy)">List of Videos</h2>
<div class="abs corner" style="left:701px;top:230px"></div>

<div class="abs video" style="top:288px" role="img" aria-label="Video still of a vintage biplane">
  <svg class="abs" style="left:80px;top:38px" width="36" height="36" viewBox="0 0 36 36" aria-hidden="true"><circle cx="18" cy="18" r="17" fill="rgba(255,255,255,.15)"/><path d="M14 10 26 18 14 26Z" fill="rgba(255,255,255,.7)"/></svg>
  <div class="abs video-ctrl"><i></i>1:26 / 3:22 &nbsp;&nbsp;&nbsp;&nbsp;&nbsp;&nbsp; HD</div>
</div>
<div class="abs v-title" style="top:292px;color:#d4232a">This is Pixelforge's version &nbsp;of Lorem Ipsum.</div>
<div class="abs v-text" style="top:322px">This is Pixelforge's version &nbsp;of Lorem Ipsum. Proin gravida nibh vel velit auctor aliquet. Aenean sollicitudin, lorem quis bibendum auctor, nisi elit consequat ipsum.</div>
<div class="abs watch" style="top:382px;background:#d4232a">Watch</div>

<div class="abs video" style="top:428px" role="img" aria-label="Video still of a vintage biplane">
  <svg class="abs" style="left:80px;top:38px" width="36" height="36" viewBox="0 0 36 36" aria-hidden="true"><circle cx="18" cy="18" r="17" fill="rgba(255,255,255,.15)"/><path d="M14 10 26 18 14 26Z" fill="rgba(255,255,255,.7)"/></svg>
  <div class="abs video-ctrl"><i></i>1:26 / 3:22 &nbsp;&nbsp;&nbsp;&nbsp;&nbsp;&nbsp; HD</div>
</div>
<div class="abs v-title" style="top:433px;color:#79b829">This is Pixelforge's version &nbsp;of Lorem Ipsum.</div>
<div class="abs v-text" style="top:463px">This is Pixelforge's version &nbsp;of Lorem Ipsum. Proin gravida nibh vel velit auctor aliquet. Aenean sollicitudin, lorem quis bibendum auctor, nisi elit consequat ipsum.</div>
<div class="abs watch" style="top:522px;background:#79b829">Watch</div>

<div class="abs video" style="top:569px" role="img" aria-label="Video still of a vintage biplane">
  <svg class="abs" style="left:80px;top:38px" width="36" height="36" viewBox="0 0 36 36" aria-hidden="true"><circle cx="18" cy="18" r="17" fill="rgba(255,255,255,.15)"/><path d="M14 10 26 18 14 26Z" fill="rgba(255,255,255,.7)"/></svg>
  <div class="abs video-ctrl"><i></i>1:26 / 3:22 &nbsp;&nbsp;&nbsp;&nbsp;&nbsp;&nbsp; HD</div>
</div>
<div class="abs v-title" style="top:573px;color:#2a7bd1">This is Pixelforge's version &nbsp;of Lorem Ipsum.</div>
<div class="abs v-text" style="top:603px">This is Pixelforge's version &nbsp;of Lorem Ipsum. Proin gravida nibh vel velit auctor aliquet. Aenean sollicitudin, lorem quis bibendum auctor, nisi elit consequat ipsum.</div>
<div class="abs watch" style="top:662px;background:#2a7bd1">Watch</div>

<!-- Images -->
<section class="abs panel" style="left:356px;top:728px;width:362px;height:406px"></section>
<h2 class="abs panel-title" style="left:356px;top:737px;width:201px;background:var(--gold)">List of Images</h2>
<div class="abs corner" style="left:701px;top:729px"></div>

<div class="abs thumb" style="left:378px;top:800px" role="img" aria-label="Portrait photo"><span>LEV AMARI<br>UI/UX Designer</span></div>
<div class="abs thumb" style="left:462px;top:800px" role="img" aria-label="Portrait photo"><span>LEV AMARI<br>UI/UX Designer</span></div>
<div class="abs thumb" style="left:546px;top:800px" role="img" aria-label="Portrait photo"><span>LEV AMARI<br>UI/UX Designer</span></div>
<div class="abs thumb" style="left:630px;top:800px" role="img" aria-label="Portrait photo"><span>LEV AMARI<br>UI/UX Designer</span></div>
<div class="abs thumb" style="left:378px;top:883px" role="img" aria-label="Portrait photo"><span>LEV AMARI<br>UI/UX Designer</span></div>
<div class="abs thumb" style="left:462px;top:883px" role="img" aria-label="Portrait photo"><span>LEV AMARI<br>UI/UX Designer</span></div>
<div class="abs thumb" style="left:546px;top:883px" role="img" aria-label="Portrait photo"><span>LEV AMARI<br>UI/UX Designer</span></div>
<div class="abs thumb" style="left:630px;top:883px" role="img" aria-label="Portrait photo"><span>LEV AMARI<br>UI/UX Designer</span></div>
<div class="abs thumb" style="left:378px;top:966px" role="img" aria-label="Portrait photo"><span>LEV AMARI<br>UI/UX Designer</span></div>
<div class="abs thumb" style="left:462px;top:966px" role="img" aria-label="Portrait photo"><span>LEV AMARI<br>UI/UX Designer</span></div>
<div class="abs thumb" style="left:546px;top:966px" role="img" aria-label="Portrait photo"><span>LEV AMARI<br>UI/UX Designer</span></div>
<div class="abs thumb" style="left:630px;top:966px" role="img" aria-label="Portrait photo"><span>LEV AMARI<br>UI/UX Designer</span></div>
<div class="abs thumb" style="left:378px;top:1048px" role="img" aria-label="Portrait photo"><span>LEV AMARI<br>UI/UX Designer</span></div>
<div class="abs thumb" style="left:462px;top:1048px" role="img" aria-label="Portrait photo"><span>LEV AMARI<br>UI/UX Designer</span></div>
<div class="abs thumb" style="left:546px;top:1048px" role="img" aria-label="Portrait photo"><span>LEV AMARI<br>UI/UX Designer</span></div>
<div class="abs thumb" style="left:630px;top:1048px" role="img" aria-label="Portrait photo"><span>LEV AMARI<br>UI/UX Designer</span></div>

<footer class="abs footer">
  <span class="abs" style="left:40px">Copyright © 2013 Studio Ledger. All Rights Reserved.</span>
  <span class="abs" style="left:511px">About Us &nbsp;| &nbsp;Advertise &nbsp;| &nbsp;Write For Us &nbsp;| &nbsp;Contact Us</span>
</footer>

</body>
</html>
```